6 Banners for $150,000 Media Campaign in Sydney

Please design a series of call to action banners to advertise this campaign and encourage people to join the CHIROPRACTIC CAMPAIGN

https://www.fundhollow.example/projects/sydney-spinal-wellness-drive-2015

banner must rotate with 3 screens and not be longer than 30 seconds in total and less than 45kb

The call to action must be "Join The Campaign"

These are the sizes:
160x600.gif
728x90.gif
300x250.gif
320x50.gif
300x600.gif

600x315.jpeg (and text can only be 20% of image area - https://www.chatterlane.example/ads/tools/text_overlay)

FRAME 1:
12 WEEK Chiropractic Campaign (Sydney)
Start June 2015

FRAME 2:
"KEEP YOUR BACK HAPPY"

FRAME 3:
Strictly limited to 300 members

CALL TO ACTION:
JOIN NOW

Target Market(s)

business owners: chiropractors

Industry/Entity Type

Media

Font styles to use
Sans Serif

Requirements
Must have
• strong call to action
• please present ALL banners in a SINGLE file / image

```html
<!DOCTYPE html>
<html lang="en">
<head>
<meta charset="utf-8">
<title>12 Week Chiropractic Campaign – Banner Set</title>
<link rel="stylesheet" href="https://fonts.googleapis.com/css2?family=Roboto+Condensed:wght@400;700&display=swap">
<style>
  :root{
    --board:#a9a9a7;
    --navy:#232f3e;
    --yellow:#f6d70b;
    --white:#ffffff;
    --rule:#d9dde2;
    --green:#7cc242;
    --green-dark:#4e9a2a;
    --label:#1e1e1e;
  }
  *{box-sizing:border-box;margin:0;padding:0}
  html,body{width:1200px;height:1000px;overflow:hidden;background:var(--board)}
  body{position:relative;font-family:"Roboto Condensed",Arial,sans-serif}
  .size-label{position:absolute;font-size:15px;color:var(--label);letter-spacing:.3px}
  .banner{position:absolute;overflow:hidden;background:#f4f2ef}
  .banner .photo{position:absolute;inset:0;
    background:
      radial-gradient(ellipse at 30% 75%, rgba(90,160,175,.55), transparent 45%),
      radial-gradient(ellipse at 22% 55%, rgba(210,60,60,.35), transparent 30%),
      radial-gradient(ellipse at 65% 80%, rgba(200,185,150,.55), transparent 40%),
      linear-gradient(180deg,#f7f6f3 0%,#ecebe6 60%,#dedbd3 100%);}
  .banner svg.panel{position:absolute;inset:0;width:100%;height:100%}
  .banner svg.panel path{fill:var(--navy)}
  .copy{position:absolute;text-align:right;color:var(--white);font-weight:700;line-height:.98}
  .copy .hi{color:var(--yellow);display:block}
  .copy .main{display:block}
  .start{display:inline-block;border-top:1.5px solid var(--rule);border-bottom:1.5px solid var(--rule);font-weight:700;color:var(--white)}
  .city{display:block;font-weight:400;color:var(--white)}
  .cta{display:inline-block;background:linear-gradient(180deg,var(--green),var(--green-dark));color:var(--navy);font-weight:700;line-height:1}
</style>
</head>
<body>

<!-- Leaderboard -->
<div class="size-label" style="left:25px;top:19px">AD 728X90</div>
<div class="banner" style="left:28px;top:45px;width:720px;height:90px">
  <div class="photo" role="img" aria-label="Photo: group of smiling adults of all ages raising their arms on a white sofa"></div>
  <svg class="panel" viewBox="0 0 720 90" preserveAspectRatio="none"><path d="M0 0H345Q318 40 312 90H0Z"/></svg>
  <div class="copy" style="right:551px;top:9px;font-size:23px"><span class="hi" style="font-size:26px">12 Week</span><span class="main">Chiropractic<br>Campaign</span></div>
  <div style="position:absolute;left:189px;top:35px;text-align:center;width:88px">
    <span class="start" style="font-size:13px;padding:3px 0">Start June 2015</span>
    <span class="city" style="font-size:8px;letter-spacing:3px;margin-top:3px">SYDNEY</span>
  </div>
</div>

<!-- Skyscraper -->
<div class="size-label" style="left:28px;top:160px">AD 160X600</div>
<div class="banner" style="left:28px;top:188px;width:160px;height:600px">
  <div class="photo" role="img" aria-label="Photo: group of smiling adults raising their arms"></div>
  <svg class="panel" viewBox="0 0 160 600" preserveAspectRatio="none"><path d="M0 0H160V398Q90 432 0 455Z"/></svg>
  <div class="copy" style="right:5px;top:44px;font-size:27px"><span class="hi" style="font-size:36px">12 Week</span><span class="main">Chiropractic<br>Campaign</span></div>
  <div style="position:absolute;right:8px;top:158px;text-align:right">
    <span class="start" style="font-size:16px;padding:4px 0">Start June 2015</span>
    <span class="city" style="font-size:10px;letter-spacing:3.5px;margin-top:6px">SYDNEY</span>
  </div>
</div>

<!-- Mobile -->
<div class="size-label" style="left:219px;top:160px">AD 350X50</div>
<div class="banner" style="left:219px;top:186px;width:320px;height:51px">
  <div class="photo" role="img" aria-label="Photo: group of smiling adults raising their arms"></div>
  <svg class="panel" viewBox="0 0 320 51" preserveAspectRatio="none"><path d="M0 0H170Q155 25 150 51H0Z"/></svg>
  <div class="copy" style="right:241px;top:5px;font-size:12px"><span class="hi" style="font-size:14px">12 Week</span><span class="main">Chiropractic<br>Campaign</span></div>
  <div style="position:absolute;left:88px;top:20px;text-align:center;width:62px">
    <span class="start" style="font-size:8px;padding:2px 0">Start June 2015</span>
    <span class="city" style="font-size:5px;letter-spacing:2px;margin-top:2px">SYDNEY</span>
  </div>
</div>

<!-- Half page -->
<div class="size-label" style="left:231px;top:251px">AD 300X600</div>
<div class="banner" style="left:226px;top:279px;width:300px;height:600px">
  <div class="photo" role="img" aria-label="Photo: group of smiling adults raising their arms on a white sofa"></div>
  <svg class="panel" viewBox="0 0 300 600" preserveAspectRatio="none"><path d="M0 0H300V290C260 300 210 302 160 288C90 268 30 228 0 168Z"/></svg>
  <div class="copy" style="right:22px;top:36px;font-size:45px"><span class="hi" style="font-size:55px">12 Week</span><span class="main">Chiropractic<br>Campaign</span></div>
  <div style="position:absolute;right:26px;top:194px;text-align:center;width:150px">
    <span class="start" style="font-size:21px;padding:6px 2px">Start June 2015</span>
    <span class="city" style="font-size:13px;letter-spacing:5px;margin-top:9px">SYDNEY</span>
  </div>
</div>

<!-- Social -->
<div class="size-label" style="left:571px;top:157px">FACEBOOK AD 600X315</div>
<div class="banner" style="left:560px;top:186px;width:600px;height:315px">
  <div class="photo" role="img" aria-label="Photo: group of smiling adults of all ages raising their arms on a white sofa"></div>
  <svg class="panel" viewBox="0 0 600 315" preserveAspectRatio="none"><path d="M400 0H600V315H430C375 270 350 200 358 140C366 80 384 40 400 0Z"/></svg>
  <div class="copy" style="right:13px;top:66px;font-size:38px"><span class="hi" style="font-size:46px">12 Week</span><span class="main">Chiropractic<br>Campaign</span></div>
  <div style="position:absolute;right:14px;top:183px;text-align:center;width:104px">
    <span class="start" style="font-size:15px;padding:3px 0">Start June 2015</span>
    <span class="city" style="font-size:11px;letter-spacing:3.5px;margin-top:3px">SYDNEY</span>
    <span class="cta" style="font-size:17px;padding:2px 5px;margin-top:4px">JOIN NOW</span>
  </div>
</div>

<!-- Medium rectangle frame 1 -->
<div class="size-label" style="left:547px;top:516px">AD 300X250</div>
<div class="banner" style="left:547px;top:541px;width:300px;height:250px">
  <div class="photo" role="img" aria-label="Photo: group of smiling adults raising their arms"></div>
  <svg class="panel" viewBox="0 0 300 250" preserveAspectRatio="none"><path d="M110 0H300V204H210C140 194 90 154 85 104C82 62 95 25 110 0Z"/></svg>
  <div class="copy" style="right:9px;top:17px;font-size:33px"><span class="hi" style="font-size:40px">12 Week</span><span class="main">Chiropractic<br>Campaign</span></div>
  <div style="position:absolute;right:13px;top:141px;text-align:center;width:118px">
    <span class="start" style="font-size:17px;padding:3px 0">Start June 2015</span>
    <span class="city" style="font-size:11px;letter-spacing:4px;margin-top:5px">SYDNEY</span>
  </div>
</div>

<!-- Medium rectangle frame 2 -->
<div class="banner" style="left:873px;top:537px;width:300px;height:250px">
  <div class="photo" role="img" aria-label="Photo: group of smiling adults raising their arms"></div>
  <svg class="panel" viewBox="0 0 300 250" preserveAspectRatio="none"><path d="M88 0H300V205H200C140 195 95 160 90 110C86 66 82 30 88 0Z"/></svg>
  <div class="copy" style="right:14px;top:14px;font-size:42px"><span class="hi" style="font-size:46px">Keep</span><span class="main">Your Back<br>Happy</span></div>
</div>

<!-- Medium rectangle frame 3 -->
<div class="banner" style="left:717px;top:798px;width:300px;height:202px">
  <div class="photo" role="img" aria-label="Photo: group of smiling adults raising their arms"></div>
  <svg class="panel" viewBox="0 0 300 202" preserveAspectRatio="none"><path d="M90 0H300V202H190C130 185 92 130 86 70C84 40 86 20 90 0Z"/></svg>
  <div class="copy" style="right:8px;top:12px;font-size:31px"><span class="hi" style="font-size:44px">Strictly</span><span class="main">Limited to 300<br>Members</span></div>
  <div style="position:absolute;right:0;top:131px">
    <span class="cta" style="font-size:20px;padding:2px 10px">JOIN NOW</span>
  </div>
</div>

</body>
</html>
```